Roofing Company Modern look

I want a modern and sophisticated look for our roofing business.

Our address is :

4276 Pellman Crossing Rd
Orlando, Fl 32825

(407)-583-2716

www.SummitcrestShinglesFl.com

I also want to make sure on the back there is a spot to put
Project Manager Name :

Number:

Because the cards will be used by all sales people

Project Manager Name :

Also there are accreditation we have logos are uploaded here as well that I would like maybe on the back of card as well

I also want to highlight our special attributions or trades:

Residential & Commercial
Fully Insured
License # CCC4872196
Insurance Claims
Serving Central Florida Since 1992
Free Estimates

Contact Information for Business Card

Our address is :

4276 Pellman Crossing Rd
Orlando, Fl 32825

(407)-583-2716

Project Manager Name :

Residential & Commercial
Fully Insured
License # CCC4872196
Insurance Claims
Free Estimates

Font styles to use
Serif
Sans Serif

Colors
3176b5

Requirements
Must have
• Must have royal blue like my logo grey and black are the colors I like

```html
<!DOCTYPE html>
<html lang="en">
<head>
<meta charset="utf-8">
<title>Summitcrest Shingles &amp; Gutters — Business Card</title>
<link rel="stylesheet" href="https://fonts.googleapis.com/css2?family=Raleway:wght@300;500;600;700&family=Lustria&display=swap">
<style>
  :root {
    --royal: #3176b5;
    --royal-deep: #0a5db4;
    --sky: #2cb3ea;
    --ink: #000000;
    --paper: #ffffff;
    --text-dark: #222222;
    --rule: #1a1a1a;
    --faint: rgba(49, 118, 181, 0.12);
  }
  * { box-sizing: border-box; margin: 0; padding: 0; }
  html, body { width: 957px; height: 1200px; overflow: hidden; background: var(--paper); }
  body { position: relative; font-family: "Raleway", Arial, sans-serif; }

  .card { position: absolute; left: 99px; width: 757px; height: 474px; overflow: hidden; }
  .card-front { top: 91px; background: var(--ink); }
  .card-back { top: 636px; background: var(--paper); border: 1px solid #ececec; }
  .accent-bar { position: absolute; left: 0; bottom: 0; width: 100%; height: 12px;
    background: linear-gradient(90deg, var(--royal-deep), var(--sky)); }

  /* Front */
  .brand-mark { position: absolute; left: 118px; top: 86px; width: 120px; height: 120px;
    border-radius: 50%; background: var(--royal); }
  .brand-name { position: absolute; left: 284px; top: 118px; color: var(--royal);
    font-weight: 700; text-transform: uppercase; line-height: 1; }
  .brand-name .primary { display: block; font-size: 44px; letter-spacing: 1px; }
  .brand-name .secondary { display: block; font-size: 21px; letter-spacing: 0.5px; margin-top: 8px; }
  .brand-rule { position: absolute; left: 287px; top: 207px; width: 404px; height: 2px; background: var(--paper); }

  .contact { position: absolute; left: 329px; color: var(--paper); font-weight: 600; font-size: 23px; line-height: 27px; }
  .contact-address { top: 260px; }
  .contact-phone { top: 331px; }
  .contact-web { top: 375px; }
  .contact-icon { position: absolute; left: -50px; top: 0; width: 38px; height: 32px; }

  /* Back */
  .pm-label { position: absolute; left: 60px; top: 48px; font-family: "Lustria", Georgia, serif;
    font-size: 34px; line-height: 34px; color: var(--text-dark); }
  .pm-line { position: absolute; left: 62px; width: 280px; height: 2px; background: var(--rule); }
  .pm-line.first { top: 171px; }
  .pm-line.second { top: 235px; }
  .brand-watermark { position: absolute; left: 60px; top: 240px; width: 285px; text-align: center;
    color: var(--faint); font-weight: 700; text-transform: uppercase; line-height: 1; }
  .brand-watermark .primary { display: block; font-size: 31px; }
  .brand-watermark .secondary { display: block; font-size: 12px; letter-spacing: 2px; margin-top: 6px; }

  .trades { position: absolute; left: 405px; top: 54px; width: 352px; height: 235px;
    background: linear-gradient(90deg, var(--royal-deep), var(--sky)); list-style: none; padding: 18px 0 0 0; }
  .trades li { position: relative; padding-left: 63px; color: var(--paper); font-weight: 300;
    font-size: 19.5px; line-height: 21px; margin-bottom: 9px; }
  .trades li::before { content: ""; position: absolute; left: 36px; top: 4px; width: 13px; height: 11px;
    border-radius: 50%; background: var(--paper);
    box-shadow: inset 0 0 0 3px var(--paper), inset 0 5px 0 0 var(--paper), inset 0 -5px 0 0 var(--paper); }
  .trades li::after { content: ""; position: absolute; left: 39px; top: 9px; width: 7px; height: 1.5px; background: var(--royal-deep); }

  .badges { position: absolute; left: 0; top: 0; width: 100%; height: 100%; pointer-events: none; }
  .badge { position: absolute; }
  .badge-seal { left: 64px; top: 331px; width: 104px; height: 104px; border-radius: 50%;
    background: #4d6f6a; border: 6px solid #cfd9d6; }
  .badge-diamond { left: 215px; top: 334px; width: 110px; height: 97px; }
  .badge-accredited { left: 342px; top: 333px; width: 79px; height: 102px; border-radius: 6px;
    background: var(--paper); border: 2px solid #1b5c8a; }
  .badge-authorized { left: 454px; top: 348px; width: 243px; height: 69px;
    border: 3px solid #1c2e5c; background: #d32027; }
</style>
</head>
<body>

<section class="card card-front" aria-label="Business card front">
  <div class="brand-mark" aria-hidden="true"></div>
  <div class="brand-name">
    <span class="primary">Summitcrest</span>
    <span class="secondary">Shingles &amp; Gutters LLC.</span>
  </div>
  <div class="brand-rule"></div>

  <div class="contact contact-address">
    <svg class="contact-icon" viewBox="0 0 38 32" fill="none" stroke="#3b8fd6" stroke-width="2.2">
      <rect x="1.5" y="13" width="14" height="14"/>
      <rect x="5" y="17" width="6" height="4" fill="#3b8fd6"/>
      <path d="M15.5 27 V13 L26 3 L36.5 13 V27 Z"/>
      <rect x="23" y="19" width="5" height="8" fill="#3b8fd6"/>
    </svg>
    4276 Pellman Crossing Rd<br>Orlando, Fl 32825
  </div>
  <div class="contact contact-phone">
    <svg class="contact-icon" viewBox="0 0 38 36" fill="none" stroke="#3b8fd6" stroke-width="2.2" stroke-linecap="round">
      <path d="M4 5 L10 2 L15 10 L11 14 Q14 21 21 25 L25 21 L33 26 L30 32 Q16 32 4 5 Z"/>
      <path d="M20 4 Q28 5 30 13"/>
      <path d="M20 9 Q24 10 25 13"/>
    </svg>
    (407)-583-2716
  </div>
  <div class="contact contact-web">
    <svg class="contact-icon" viewBox="0 0 38 34" fill="none" stroke="#3b8fd6" stroke-width="2.2">
      <circle cx="17" cy="17" r="15"/>
      <path d="M9 8 Q14 12 12 17 Q10 22 14 28" />
      <path d="M24 6 Q21 12 25 15 Q28 19 25 25"/>
    </svg>
    www.SummitcrestShinglesFl.com
  </div>

  <div class="accent-bar"></div>
</section>

<section class="card card-back" aria-label="Business card back">
  <p class="pm-label">Project Manager<br>Name :</p>
  <div class="brand-watermark" aria-hidden="true">
    <span class="primary">Summitcrest</span>
    <span class="secondary">Shingles &amp; Gutters Inc.</span>
  </div>
  <div class="pm-line first"></div>
  <div class="pm-line second"></div>

  <ul class="trades">
    <li>Residential &amp; Commercial</li>
    <li>Fully Insured</li>
    <li>License # CCC4872196</li>
    <li>Insurance Claims</li>
    <li>Serving Central Florida<br>Since 1992</li>
    <li>Free Estimates</li>
  </ul>

  <div class="badge badge-seal" role="img" aria-label="Screened and approved listing badge"></div>
  <svg class="badge badge-diamond" viewBox="0 0 110 97" role="img" aria-label="Master shingle applicator certification badge">
    <polygon points="55,0 110,48.5 55,97 0,48.5" fill="#1a1a1a"/>
    <rect x="2" y="20" width="106" height="57" fill="#1d3f73"/>
  </svg>
  <div class="badge badge-accredited" role="img" aria-label="Accredited business badge"></div>
  <div class="badge badge-authorized" role="img" aria-label="Authorized roofing contractor badge"></div>

  <div class="accent-bar"></div>
</section>

</body>
</html>
```